A weight loss and fitness website design

I am into different types of modern weight loss techniques for people who are a little fatty and wish to be physically and mentally fit. Basically, the website is to teach people how to reduce weight using different methods such as diet, exercises, yoga and other forms. I would need an eye catching website which would make visitors want to come back. The will be also be different forms of exercises for a health and fit life. This said, my website is to have two categories of
1) weight loss techniques
2) exercise of fit and healthy living.
I prefer bright colors such as green, blue, yellow, and orange. Imagery should include before and after pictures of people suffering from obesity, people under going exercises.
Designers can get ideas and inspiration from the website fitmerlo.com which i was previously part of the team.
Target Market(s)
My target audience are people suffering from obesity, malnutrition and physical deficiency.
Industry/Entity Type
Fitness
Coding
Coded - Design and coding required
Number of Pages Required
1 page
Look and feel

```html
<!DOCTYPE html>
<html lang="en">
<head>
<meta charset="utf-8">
<title>Trimvale Fitness</title>
<link href="https://fonts.googleapis.com/css2?family=Open+Sans:wght@400;600;700&display=swap" rel="stylesheet">
<style>
:root{
  --blue:#1b8fd6;
  --blue-dark:#1479b8;
  --green:#3db34a;
  --orange:#f26522;
  --white:#ffffff;
  --ink:#333333;
  --muted:#8a8a8a;
  --footer:#3b3b3b;
  --footer-text:#c9c9c9;
  --card:#2b2b2b;
}
*{box-sizing:border-box;margin:0;padding:0}
html,body{width:1200px;height:4000px;overflow:hidden}
body{font-family:"Open Sans",Arial,sans-serif;color:var(--ink);background:var(--white);position:relative}
section,header,footer{position:absolute;left:0;width:1200px}
.btn{display:inline-block;font-size:13px;font-weight:700;color:var(--white);padding:11px 20px;border-radius:2px;letter-spacing:.5px;text-transform:uppercase}
.btn-orange{background:var(--orange)}
.btn-green{background:var(--green)}
.photo{position:absolute}

/* header */
.site-header{top:0;height:80px;background:var(--white);box-shadow:0 1px 4px rgba(0,0,0,.12);z-index:2}
.brand{position:absolute;left:130px;top:22px;font-size:28px;font-weight:700;color:var(--blue);display:flex;align-items:center;gap:8px;white-space:nowrap}
.brand-dot{width:14px;height:14px;border-radius:50%;background:var(--orange)}
.main-nav{position:absolute;left:420px;top:26px;display:flex;gap:0;white-space:nowrap}
.main-nav a{font-size:13px;color:var(--ink);padding:6px 9px;line-height:18px}
.main-nav a.active{background:var(--green);color:var(--white)}
.phone-pill{position:absolute;left:940px;top:24px;background:var(--blue);color:var(--white);font-size:14px;font-weight:700;padding:7px 14px;border-radius:3px;display:flex;align-items:center;gap:8px;white-space:nowrap}

/* hero */
.hero{top:80px;height:520px;overflow:hidden}
.hero .photo{inset:0;background:linear-gradient(90deg,#9ea3a6 0%,#c9cbcc 45%,#e7e7e6 60%,#b9b1a8 100%)}
.hero h1{position:absolute;left:170px;top:150px;font-size:58px;line-height:68px;font-weight:700;color:var(--white);text-shadow:0 2px 6px rgba(0,0,0,.25)}
.hero .btn{position:absolute;left:170px;top:318px}
.slider-arrow{position:absolute;top:240px;width:44px;height:44px;border-radius:50%;background:rgba(0,0,0,.25);display:flex;align-items:center;justify-content:center}
.slider-arrow.prev{left:40px}
.slider-arrow.next{right:40px}

/* categories */
.categories{top:600px;height:900px;background:var(--blue);color:var(--white)}
.category{position:absolute;left:0;width:1200px}
.category .icon-ring{width:56px;height:56px;border:2px solid var(--white);border-radius:50%;display:flex;align-items:center;justify-content:center}
.category h2{font-size:28px;font-weight:600;margin:16px 0 18px}
.category p{font-size:13px;line-height:21px;max-width:580px;opacity:.92}
.category .btn{margin-top:28px}
.category-one{top:40px}
.category-one .photo{left:150px;top:30px;width:220px;height:260px;background:linear-gradient(160deg,#58a9dd,#2c7fb6);border-radius:4px}
.category-one .copy{position:absolute;left:470px;top:20px}
.divider{position:absolute;left:130px;top:450px;width:940px;height:1px;background:rgba(255,255,255,.35)}
.category-two{top:480px}
.category-two .copy{position:absolute;left:150px;top:20px}
.category-two .photo{left:840px;top:10px;width:250px;height:340px;background:linear-gradient(160deg,#5eb0e2,#2a7ab0);border-radius:4px}

/* welcome */
.welcome{top:1500px;height:560px;text-align:center}
.welcome h2{font-size:34px;font-weight:600;color:var(--blue);margin-top:55px}
.welcome p{font-size:13px;line-height:21px;color:var(--muted);width:640px;margin:14px auto 0}
.welcome .photo{left:300px;top:170px;width:660px;height:390px;background:linear-gradient(180deg,#ffffff 0%,#f1eff2 55%,#e5d7e4 85%,#ffffff 100%)}

/* reduce weight */
.reduce{top:2060px;height:540px;background:var(--green);color:var(--white)}
.reduce h2{text-align:center;font-size:30px;font-weight:600;margin-top:58px}
.cards{position:absolute;left:132px;top:130px;display:flex;gap:12px}
.card{position:relative;width:304px;height:320px;background:linear-gradient(180deg,#4a4a4a,var(--card));text-align:center;padding-top:90px}
.card .icon-ring{width:62px;height:62px;margin:0 auto;border:2px solid var(--white);border-radius:50%;display:flex;align-items:center;justify-content:center}
.card h3{font-size:24px;font-weight:600;margin-top:10px}
.card p{font-size:13px;line-height:19px;width:200px;margin:6px auto 0;opacity:.9}

/* testimonials */
.testimonials{top:2600px;height:530px;overflow:hidden}
.testimonials .photo{inset:0;background:linear-gradient(180deg,#ffffff 0%,#f3f4f4 25%,#dfe6ea 45%,#9fb5c4 62%,#8a7260 78%,#6b5444 100%)}
.testimonials h2{position:absolute;left:125px;top:38px;font-size:30px;font-weight:600;color:var(--blue)}
.quote-box{position:absolute;left:130px;top:100px;width:300px;height:290px;background:var(--white);box-shadow:0 2px 10px rgba(0,0,0,.12);padding:26px 28px}
.quote-mark{font-size:64px;line-height:40px;color:#c8c8c8;font-weight:700}
.quote-box p{font-size:13px;line-height:20px;color:var(--muted);margin-top:16px}
.author{display:flex;align-items:center;gap:12px;margin-top:32px}
.author .avatar{width:38px;height:38px;border-radius:50%;background:#9aa6ae}
.author strong{display:block;font-size:13px;color:var(--ink)}
.author span{font-size:12px;color:var(--muted)}

/* before after */
.results{top:3130px;height:570px;background:var(--blue);color:var(--white)}
.results .photo{left:150px;top:30px;width:360px;height:510px;background:linear-gradient(180deg,#3a9ad9,#2a85c6);border-radius:4px}
.results .copy{position:absolute;left:640px;top:190px;width:450px}
.results h2{font-size:30px;font-weight:600}
.results p{font-size:13px;line-height:21px;margin-top:16px;opacity:.92}
.results .btn{margin-top:26px}

/* footer */
.site-footer{top:3700px;height:300px;background:var(--footer);color:var(--footer-text);font-size:13px}
.footer-brand{position:absolute;left:130px;top:40px}
.footer-brand .brand{position:static;color:var(--white)}
.follow{margin-top:22px;color:var(--white);font-weight:600}
.socials{display:flex;gap:10px;margin-top:12px}
.socials span{width:30px;height:30px;border-radius:50%;background:#5a5a5a}
.footer-col{position:absolute;top:44px}
.footer-col h4{color:var(--white);font-size:16px;font-weight:600;margin-bottom:16px}
.footer-col li{list-style:none;line-height:23px;display:flex;gap:8px;align-items:flex-start}
.col-contact{left:450px;width:190px}
.col-menu{left:660px}
.col-news{left:890px;width:190px}
.news-input{height:38px;border:1px solid #5c5c5c;background:#2f2f2f;color:#9a9a9a;padding:9px 12px;font-size:13px}
.news-btn{margin-top:12px;height:40px;background:var(--orange);color:var(--white);font-weight:700;font-size:15px;text-align:center;line-height:40px}
.copyright{position:absolute;left:130px;bottom:18px;font-size:12px;color:#9a9a9a}
</style>
</head>
<body>

<header class="site-header">
  <div class="brand"><span class="brand-dot"></span>Trimvale Fitness</div>
  <nav class="main-nav">
    <a class="active">Home</a><a>About Us</a><a>Training</a><a>Weight Loss</a><a>Testimonials</a><a>Contact Us</a>
  </nav>
  <div class="phone-pill">
    <svg width="14" height="14" viewBox="0 0 24 24"><path fill="#fff" d="M6.6 10.8a15 15 0 006.6 6.6l2.2-2.2c.3-.3.7-.4 1-.2 1.1.4 2.3.6 3.6.6.6 0 1 .4 1 1V20c0 .6-.4 1-1 1A17 17 0 013 4c0-.6.4-1 1-1h3.5c.6 0 1 .4 1 1 0 1.3.2 2.5.6 3.6.1.3 0 .7-.2 1z"/></svg>
    1 800 555 0147
  </div>
</header>

<section class="hero">
  <div class="photo" role="img" aria-label="Muscular man lifting a kettlebell against a light grey studio backdrop"></div>
  <h1>Physically and<br>Mentally Fit.</h1>
  <span class="btn btn-orange">Learn More</span>
  <div class="slider-arrow prev"><svg width="16" height="16" viewBox="0 0 16 16"><path d="M10 2L4 8l6 6" stroke="#fff" stroke-width="2" fill="none"/></svg></div>
  <div class="slider-arrow next"><svg width="16" height="16" viewBox="0 0 16 16"><path d="M6 2l6 6-6 6" stroke="#fff" stroke-width="2" fill="none"/></svg></div>
</section>

<section class="categories">
  <div class="category category-one">
    <div class="photo" role="img" aria-label="Woman in sportswear doing a plank push-up"></div>
    <div class="copy">
      <div class="icon-ring"><svg width="28" height="28" viewBox="0 0 28 28"><rect x="4" y="4" width="20" height="20" rx="4" stroke="#fff" stroke-width="2" fill="none"/><circle cx="14" cy="13" r="5" stroke="#fff" stroke-width="2" fill="none"/><path d="M14 13l2-3" stroke="#fff" stroke-width="2"/></svg></div>
      <h2>Weight Loss Techniques</h2>
      <p>Simple daily habits, smarter meals and steady movement add up to real, lasting results. Our guided weight loss plans show you which methods work for your body, how to track progress without stress and how to keep going when motivation drops. Every step is explained clearly, so you can start today at home.</p>
      <span class="btn btn-green">Learn More</span>
    </div>
  </div>
  <div class="divider"></div>
  <div class="category category-two">
    <div class="copy">
      <div class="icon-ring"><svg width="28" height="28" viewBox="0 0 28 28"><circle cx="14" cy="14" r="10" stroke="#fff" stroke-width="2" fill="none"/><path d="M9 14l4 4 7-8" stroke="#fff" stroke-width="2" fill="none"/></svg></div>
      <h2>Exercise of fit and healthy living.</h2>
      <p>Strength, balance and stamina grow with regular practice. Follow short routines built for every level, from gentle first steps to full workouts, and learn how rest, sleep and water support a fit and healthy life. Small efforts each day build a stronger body and a calmer mind over time.</p>
      <span class="btn btn-green">Learn More</span>
    </div>
    <div class="photo" role="img" aria-label="Woman in black sportswear doing a lunge"></div>
  </div>
</section>

<section class="welcome">
  <h2>Welcome to our site</h2>
  <p>Discover practical ways to lose weight, move more and feel better every day. Here you will find clear guides, friendly routines and honest advice for lasting change.</p>
  <div class="photo" role="img" aria-label="Two people in a downward dog yoga pose on a mat"></div>
</section>

<section class="reduce">
  <h2>How to Reduce Weight</h2>
  <div class="cards">
    <div class="card" role="group" aria-label="Diet">
      <div class="icon-ring"><svg width="30" height="30" viewBox="0 0 30 30"><path d="M15 8c-6 0-8 5-7 10s4 8 7 6c3 2 6-1 7-6s-1-10-7-10z" stroke="#fff" stroke-width="2" fill="none"/><path d="M15 8c0-3 2-4 4-4" stroke="#fff" stroke-width="2" fill="none"/></svg></div>
      <h3>Diet</h3>
      <p>Balanced meals and smart portions that keep you full and on track.</p>
    </div>
    <div class="card" role="group" aria-label="Exercises">
      <div class="icon-ring"><svg width="30" height="30" viewBox="0 0 30 30"><path d="M4 15h22M7 10v10M23 10v10M10 12v6M20 12v6" stroke="#fff" stroke-width="2"/></svg></div>
      <h3>Exercises</h3>
      <p>Easy routines to burn calories and build strength at any level.</p>
    </div>
    <div class="card" role="group" aria-label="Yoga">
      <div class="icon-ring"><svg width="30" height="30" viewBox="0 0 30 30"><circle cx="15" cy="7" r="3" fill="#fff"/><path d="M15 11v8M8 14l7 3 7-3M8 24l7-5 7 5" stroke="#fff" stroke-width="2" fill="none"/></svg></div>
      <h3>Yoga</h3>
      <p>Gentle poses and breathing that improve balance, focus and calm.</p>
    </div>
  </div>
</section>

<section class="testimonials">
  <div class="photo" role="img" aria-label="Woman tying her running shoe on a wooden pier by the sea"></div>
  <h2>Testimonials</h2>
  <div class="quote-box">
    <div class="quote-mark">&ldquo;</div>
    <p>I lost twelve kilos in six months with these plans. The routines were simple to follow and I finally feel strong and confident again.</p>
    <div class="author">
      <div class="avatar"></div>
      <div><strong>Daniel Morrow</strong><span>Member</span></div>
    </div>
  </div>
</section>

<section class="results">
  <div class="photo" role="img" aria-label="Before and after photos of the same woman in sportswear"></div>
  <div class="copy">
    <h2>Before and After</h2>
    <p>Real members, real progress. See how steady training and better eating changed their lives, one week at a time. Browse their stories and find the motivation to begin your own journey today.</p>
    <span class="btn btn-green">View Gallery</span>
  </div>
</section>

<footer class="site-footer">
  <div class="footer-brand">
    <div class="brand"><span class="brand-dot"></span>Trimvale Fitness</div>
    <div class="follow">Follow us on</div>
    <div class="socials"><span></span><span></span><span></span><span></span><span></span></div>
  </div>
  <div class="footer-col col-contact">
    <h4>Contact Us</h4>
    <ul>
      <li><svg width="12" height="16" viewBox="0 0 12 16"><path d="M6 0a6 6 0 00-6 6c0 4.5 6 10 6 10s6-5.5 6-10a6 6 0 00-6-6zm0 8a2 2 0 110-4 2 2 0 010 4z" fill="#c9c9c9"/></svg>120 Harbor Lane,<br>Boston, MA 02110</li>
      <li><svg width="12" height="12" viewBox="0 0 24 24"><path fill="#c9c9c9" d="M6.6 10.8a15 15 0 006.6 6.6l2.2-2.2c.3-.3.7-.4 1-.2 1.1.4 2.3.6 3.6.6.6 0 1 .4 1 1V20c0 .6-.4 1-1 1A17 17 0 013 4c0-.6.4-1 1-1h3.5c.6 0 1 .4 1 1 0 1.3.2 2.5.6 3.6.1.3 0 .7-.2 1z"/></svg>1 800 555 0147</li>
      <li><svg width="14" height="12" viewBox="0 0 14 12"><rect x="1" y="1" width="12" height="10" stroke="#c9c9c9" fill="none"/><path d="M1 1l6 5 6-5" stroke="#c9c9c9" fill="none"/></svg>info@trimvalefitness.com</li>
    </ul>
  </div>
  <div class="footer-col col-menu">
    <h4>Menu</h4>
    <ul><li>Home</li><li>About Us</li><li>Training</li><li>Weight Loss</li><li>Blog</li><li>Contact Us</li></ul>
  </div>
  <div class="footer-col col-news">
    <h4>Newsletter Signup!</h4>
    <div class="news-input">E-mail</div>
    <div class="news-btn">SIGNUP!</div>
  </div>
  <div class="copyright">Copyright © 2024 All Rights Reserved</div>
</footer>

</body>
</html>
```